5 Planner Covers for Teacher Planners

Hello,
I currently run a Speech-Language Pathologist website and have created a planner for my fellow Speech Therapist. I would like someone to create 5 different planner covers so my followers will have different options to choose from.
Here is my planner from last year to give you an idea of what the planner will look like http://www.talkwellnook.example/free-slp-planner/
My followers are mostly women aged 25-50. However, I don't want the covers to be overly girly or excessive with flowers. Simple is better.
I'd also like there to be an editable text box to allow the Speech Therapist to type their name on their cover if they wish.
Planner Cover can say any of the following: SLP Planner, Planner, Speech Therapy Planner, Speech-Language Pathologist (maybe this title could be editable as well??).
To give you an idea I have uploaded a screenshot of last year's planners cover that I made myself.
What I am looking for:
-Size 8.5" by 11"
-5 different planner covers
-1 gender-neutral cover
-simple design
-limited flowers (or overly girly
-text box to add a personal name
-Possible titles: SLP Planner, Planner, Speech Therapy Planner, Speech-Language Pathologist (maybe this title could be editable as well??)
Target Market(s)
Women aged 25-50
Colors
Designer to choose colors to be used in the design.
Requirements
Must have
- What I am looking for:
-Size 8.5" by 11"
-1 gender-neutral cover
-simple design
Nice to have
- I've uploaded some that I like from Craftly to give you an idea.
Here is my craftly store https://www.craftly.example/shop/QuietMeadowHome to give you an idea of things I like.
I like Marla Hensley and her simple elegant rustic style.

```html
<!DOCTYPE html>
<html lang="en">
<head>
<meta charset="UTF-8">
<title>SLP Planner Cover</title>
<link rel="stylesheet" href="https://fonts.googleapis.com/css2?family=Great+Vibes&family=Sacramento&family=Mrs+Saint+Delafield&family=Comfortaa:wght@400&display=swap">
<style>
  :root {
    --paper: #f8f1ed;
    --paper-shade: #f1e7e2;
    --rose-deep: #985450;
    --rose-soft: #c8aaa2;
    --wash-pink: #f1c3bf;
    --wash-light: #f6dcd8;
    --flower-tone: #e9d3cf;
  }
  html, body {
    margin: 0;
    padding: 0;
    overflow: hidden;
    background: var(--paper);
  }
  .cover {
    position: relative;
    width: 927px;
    height: 1200px;
    overflow: hidden;
    background: radial-gradient(ellipse at 30% 40%, var(--paper) 0%, var(--paper-shade) 100%);
  }
  .wash {
    position: absolute;
    border-radius: 45% 55% 40% 60% / 60% 45% 55% 40%;
    filter: blur(6px);
  }
  .wash--top {
    left: 395px;
    top: -30px;
    width: 560px;
    height: 180px;
    background: radial-gradient(ellipse at 55% 45%, var(--wash-pink) 0%, var(--wash-light) 60%, rgba(246,220,216,0) 100%);
  }
  .wash--bottom {
    left: 90px;
    top: 1045px;
    width: 650px;
    height: 190px;
    background: radial-gradient(ellipse at 45% 55%, var(--wash-pink) 0%, var(--wash-light) 55%, rgba(246,220,216,0) 100%);
  }
  .illustration {
    position: absolute;
    border-radius: 50%;
    background: radial-gradient(ellipse at center, var(--flower-tone) 0%, rgba(233,211,207,0.5) 60%, rgba(233,211,207,0) 100%);
  }
  .illustration--title-iris {
    left: 482px;
    top: 276px;
    width: 138px;
    height: 110px;
  }
  .illustration--corner-irises {
    left: 0;
    top: 811px;
    width: 297px;
    height: 389px;
    border-radius: 40% 50% 0 0;
  }
  .stem-line {
    position: absolute;
    inset: 0;
    width: 927px;
    height: 1200px;
    pointer-events: none;
  }
  .title-main {
    position: absolute;
    left: 236px;
    top: 322px;
    margin: 0;
    font-family: "Great Vibes", cursive;
    font-weight: 400;
    font-size: 190px;
    line-height: 1;
    color: var(--rose-deep);
  }
  .title-sub {
    position: absolute;
    left: 442px;
    top: 418px;
    margin: 0;
    font-family: "Sacramento", cursive;
    font-size: 100px;
    line-height: 1;
    color: var(--rose-soft);
  }
  .owner-label {
    position: absolute;
    left: 492px;
    top: 884px;
    margin: 0;
    font-family: "Comfortaa", sans-serif;
    font-size: 20.5px;
    color: var(--rose-deep);
  }
  .owner-name {
    position: absolute;
    left: 592px;
    top: 930px;
    margin: 0;
    font-family: "Mrs Saint Delafield", cursive;
    font-size: 60px;
    line-height: 1.2;
    color: var(--rose-soft);
  }
</style>
</head>
<body>
  <main class="cover">
    <div class="wash wash--top" role="img" aria-label="Soft pink watercolour wash"></div>
    <div class="wash wash--bottom" role="img" aria-label="Soft pink watercolour wash"></div>

    <div class="illustration illustration--title-iris" role="img" aria-label="Small line-drawn iris flower"></div>
    <div class="illustration illustration--corner-irises" role="img" aria-label="Line-drawn iris flowers with buds and leaves"></div>

    <svg class="stem-line" viewBox="0 0 927 1200" aria-hidden="true">
      <line x1="524" y1="394" x2="354" y2="640" stroke="var(--rose-soft)" stroke-width="1.2"/>
    </svg>

    <h1 class="title-main">Slp</h1>
    <p class="title-sub">planner</p>

    <p class="owner-label">This planner belongs to</p>
    <p class="owner-name">Renata Hollis</p>
  </main>
</body>
</html>
```